Design for a real estate wev portal

Contents and features of the site
---------------------------------
Website in 5 languages: French, Dutch, English, German, Spanish.
English name of the site: Lantern Nest Place
Main purpose of the site:
- allow people to rent their house/ appartment for flatsharing purposes.
- help people wanting to find a room in flatsharing
- help people to find additional roommates for their flatsharing
Key interaction sequence:
1. I create a "group" of people who have common interest/hobbies
2. People who have the same interests/hobbies join my group
3. I look for a house/appartment to host my group
Website structure will be the following:
- Home
- Groups
-- Look for a group
--- Join a group
-- Create a group
- Properties
-- Look for a house/appartement
-- Apply
- Sales conditions
- Contact
- My account
-- My profile
-- My groups OR my properties
Your mission
------------
The client has no graphical guidelines, simply a logo (see attached).
We need a (responsive compliant) design for the following pages (we expect PSD's from you. No HTML nor CSS):
1. homepage (see example and wireframe attached)
2. properties search result list (see wireframe attached)
3. "detailed" form for properties
4. groups search result list
5. "detailed" form for groups
6. my account page
FOR THE COMPETITION step we only expect from you the design of first 2 screens.
Based on that, we will select the designer who will win the project, and will have to design the 4 remaining screens.
Target Market(s)
B2C
Industry/Entity Type
Real Estate
Number of Pages Required
5+ page
Look and feel
Each slider illustrates characteristics of the customer's brand and the style your logo design should communicate.

```html
<!DOCTYPE html>
<html lang="en">
<head>
<meta charset="utf-8">
<title>Lantern Nest Place – Properties</title>
<link rel="stylesheet" href="https://fonts.googleapis.com/css2?family=Open+Sans:wght@400;600&display=swap">
<style>
:root{
  --green:#6cbf45;
  --red:#f0553d;
  --teal:#148c9f;
  --ink:#333;
  --muted:#666;
  --line:#cfcfcf;
  --white:#fff;
}
*{box-sizing:border-box;margin:0;padding:0}
html,body{width:687px;height:1200px;overflow:hidden;background:var(--white)}
body{font-family:"Open Sans",Arial,sans-serif;color:var(--ink);position:relative}
.abs{position:absolute}
.lang-select{left:418px;top:11px;width:46px;height:14px;border:1px solid var(--line);font-size:8px;line-height:12px;padding-left:4px}
.lang-select::after{content:"";position:absolute;right:4px;top:4px;border:3px solid transparent;border-top-color:#333}
.socials{display:flex;gap:4px}
.socials span{width:12px;height:12px;border-radius:2px;display:block}
.top-socials{left:471px;top:12px}
.hero{left:0;top:51px;width:687px;height:144px;background:linear-gradient(180deg,#2a3540 0%,#1d2a33 60%,#27313a 100%)}
.hero-title{left:0;top:101px;width:687px;text-align:center;color:var(--white);font-size:22px;font-weight:400}
.hero-text{left:200px;top:137px;width:287px;text-align:center;color:var(--white);font-size:8px;line-height:12px}
.navbar{left:74px;top:37px;width:539px;height:34px;background:var(--white);border-radius:4px;box-shadow:0 1px 3px rgba(0,0,0,.2)}
.brand{left:14px;top:4px;width:96px;display:flex;align-items:center;gap:5px}
.brand i{width:8px;height:8px;border-radius:50%;background:var(--green);display:block;flex:none}
.brand span{font-size:11.5px;line-height:13px;font-weight:600;color:var(--green)}
.nav a{position:absolute;top:13px;font-size:9.5px;color:var(--ink);text-decoration:none}
.field{border:1px solid var(--line);height:23px;font-size:8px;line-height:21px;padding-left:5px;color:var(--ink);background:var(--white)}
.field.select::after{content:"";position:absolute;right:6px;top:7px;width:5px;height:5px;border-right:2px solid #bbb;border-bottom:2px solid #bbb;transform:rotate(45deg)}
.field.dark::after{border-color:#333}
.search-box{left:74px;top:230px;width:126px;text-align:center;font-size:10px;color:#999;padding:0}
.price-label{left:74px;top:438px;font-size:10px}
.slider{left:75px;top:460px;width:125px;height:6px;background:#eee;border-radius:3px}
.slider-fill{left:84px;top:460px;width:66px;height:5px;background:var(--green);border-radius:3px}
.knob{width:6px;height:6px;border-radius:50%;background:var(--teal);top:460px}
.slider-labels{left:74px;top:469px;width:128px;display:flex;justify-content:space-between;font-size:6px}
.btn{display:flex;align-items:center;justify-content:center;color:var(--white);border-radius:4px;font-size:10px}
.btn-red{background:var(--red)}
.btn-green{background:var(--green)}
.photo{border-radius:1px}
.ph-facade{background:linear-gradient(180deg,#3d5680 0%,#5a6f94 45%,#2c3f63 100%)}
.ph-chalet{background:linear-gradient(180deg,#7fa3cf 0%,#c6c9c4 45%,#5b6a4c 100%)}
.ph-villa{background:linear-gradient(180deg,#2b5088 0%,#3b567a 55%,#6f5a3a 100%)}
.ph-lounge{background:linear-gradient(180deg,#e4e2de 0%,#a8a8a6 55%,#566a7c 100%)}
.side-title{font-size:10px;left:74px}
.results-title{left:212px;top:261px;font-size:14px;font-weight:400}
.results-count{left:480px;top:264px;width:120px;text-align:right;font-size:7.5px}
.listing{left:213px;width:390px;height:82px}
.listing .photo{position:absolute;left:0;top:0;width:125px;height:82px}
.listing h3{position:absolute;left:136px;top:-1px;font-size:10px;font-weight:400}
.listing .stars{position:absolute;right:0;top:0;font-size:7.5px;letter-spacing:.5px}
.listing p{position:absolute;left:137px;top:22px;width:186px;height:36px;overflow:hidden;font-size:7.3px;line-height:12px;text-align:justify;color:var(--ink)}
.listing .meta{position:absolute;left:136px;top:64px;display:flex;gap:9px;font-size:6px;font-weight:600;align-items:center}
.listing .meta span{display:flex;align-items:center;gap:3px}
.listing .book{position:absolute;left:336px;top:24px;width:50px;height:26px}
.listing .price{position:absolute;left:336px;top:66px;width:50px;height:9px;font-size:6px;font-weight:600;border-radius:5px}
.pager{left:364px;top:940px;display:flex;gap:3px;font-size:8px;align-items:center}
.pager span{width:10px;height:11px;display:flex;align-items:center;justify-content:center}
.pager .on{background:var(--green);color:var(--white)}
.view-toggle{left:572px;top:235px}
.footer{left:0;top:1022px;width:687px;height:178px;background:var(--teal);color:var(--white)}
.footer h4{position:absolute;top:38px;font-size:14px;font-weight:400}
.footer ul{position:absolute;top:66px;list-style:none;font-size:8px;line-height:14.4px}
.mission{position:absolute;left:314px;top:68px;width:125px;font-size:7.8px;line-height:12px}
.contact-line{position:absolute;left:472px;font-size:7.5px;display:flex;gap:6px;align-items:center}
.foot-lang{left:472px;top:101px;width:45px;height:13px;background:rgba(255,255,255,.25);font-size:8px;padding-left:3px;line-height:13px}
</style>
</head>
<body>

<div class="abs hero photo" role="img" aria-label="Dim modern living room interior with large windows"></div>
<h1 class="abs hero-title">Lantern Nest Place</h1>
<p class="abs hero-text">It is a long established fact that a reader will be distracted by the read-able content of a page when looking at its layout. The point of using</p>

<div class="abs lang-select">English</div>
<div class="abs socials top-socials">
  <span style="background:#f26b2b"></span><span style="background:#d9392c"></span><span style="background:#1f6fa8"></span><span style="background:#356a9a"></span><span style="background:#4cb050"></span><span style="background:#dc4b3e"></span><span style="background:#2aa9e0"></span><span style="background:#ea5a6e"></span><span style="background:#3b5998"></span>
</div>

<header class="abs navbar">
  <div class="abs brand"><i></i><span>Lantern Nest<br>Place</span></div>
  <nav class="nav">
    <a style="left:119px">Home</a><a style="left:157px">Groups</a><a style="left:200px">Properties</a><a style="left:256px">My account</a><a style="left:317px">Contact</a><a style="left:363px">Sales conditions</a><a style="left:444px">login</a><a style="left:476px">Register</a>
  </nav>
</header>

<div class="abs field search-box">Location or Name</div>
<div class="abs field select" style="left:74px;top:265px;width:126px">10 Rooms</div>
<div class="abs field select" style="left:74px;top:300px;width:126px">Egypt</div>
<div class="abs field select" style="left:74px;top:335px;width:126px">Cairo</div>
<div class="abs field select" style="left:74px;top:370px;width:126px">Rent</div>
<div class="abs field select" style="left:74px;top:406px;width:126px">Villa</div>
<div class="abs price-label">Price</div>
<div class="abs slider"></div>
<div class="abs slider-fill"></div>
<div class="abs knob" style="left:80px"></div>
<div class="abs knob" style="left:148px"></div>
<div class="abs slider-labels"><span>10000</span><span>100000</span><span>1000000</span><span>10000000</span></div>
<div class="abs btn btn-red" style="left:74px;top:486px;width:126px;height:23px">Search</div>
<div class="abs btn btn-green" style="left:74px;top:522px;width:126px;height:23px"></div>

<div class="abs photo ph-facade" style="left:75px;top:558px;width:125px;height:83px" role="img" aria-label="Lit entrance of a stone apartment building at dusk"></div>
<div class="abs side-title" style="top:650px">House Ciro , Egypt</div>
<div class="abs btn btn-green" style="left:75px;top:673px;width:57px;height:21px"><svg width="14" height="12" viewBox="0 0 14 12"><rect x="1" y="2" width="12" height="9" fill="none" stroke="#fff"/><path d="M1 5h12M4 0v3M10 0v3" stroke="#fff"/></svg></div>
<div class="abs btn btn-red" style="left:142px;top:673px;width:57px;height:21px">100$</div>

<div class="abs photo ph-facade" style="left:75px;top:706px;width:125px;height:82px" role="img" aria-label="Lit entrance of a stone apartment building at dusk"></div>
<div class="abs side-title" style="top:797px">House Ciro , Egypt</div>
<div class="abs btn btn-green" style="left:75px;top:819px;width:57px;height:22px"><svg width="14" height="12" viewBox="0 0 14 12"><rect x="1" y="2" width="12" height="9" fill="none" stroke="#fff"/><path d="M1 5h12M4 0v3M10 0v3" stroke="#fff"/></svg></div>
<div class="abs btn btn-red" style="left:142px;top:819px;width:57px;height:22px">100$</div>

<div class="abs photo ph-facade" style="left:75px;top:853px;width:125px;height:82px" role="img" aria-label="Lit entrance of a stone apartment building at dusk"></div>
<div class="abs side-title" style="top:944px">House Ciro , Egypt</div>
<div class="abs btn btn-green" style="left:75px;top:966px;width:57px;height:22px"><svg width="14" height="12" viewBox="0 0 14 12"><rect x="1" y="2" width="12" height="9" fill="none" stroke="#fff"/><path d="M1 5h12M4 0v3M10 0v3" stroke="#fff"/></svg></div>
<div class="abs btn btn-red" style="left:142px;top:966px;width:57px;height:22px">100$</div>

<div class="abs field select dark" style="left:212px;top:230px;width:80px">100 per page</div>
<div class="abs field select dark" style="left:306px;top:230px;width:81px;font-size:7.5px">Order By Rate</div>
<svg class="abs view-toggle" width="30" height="13" viewBox="0 0 30 13">
  <g fill="#555"><rect x="0" y="0" width="2.5" height="2.5"/><rect x="4" y="0" width="10" height="2.5"/><rect x="0" y="3.5" width="2.5" height="2.5"/><rect x="4" y="3.5" width="10" height="2.5"/><rect x="0" y="7" width="2.5" height="2.5"/><rect x="4" y="7" width="10" height="2.5"/><rect x="0" y="10.5" width="2.5" height="2.5"/><rect x="4" y="10.5" width="10" height="2.5"/>
  <rect x="17" y="0" width="6" height="6"/><rect x="24" y="0" width="6" height="6"/><rect x="17" y="7" width="6" height="6"/><rect x="24" y="7" width="6" height="6"/></g>
</svg>
<h2 class="abs results-title">We found 30 Result</h2>
<div class="abs results-count">you show 10 of 30 page 1</div>

<svg width="0" height="0" style="position:absolute">
  <defs>
    <g id="i-bed"><path d="M0 8V2h2v3h4V3h6q2 0 2 2v3h-2V7H2v1z" fill="#555"/></g>
    <g id="i-bath"><path d="M2 8h8q2 0 2-3V4H4V1h2M5 8v1" fill="none" stroke="#555" stroke-width="1.2"/></g>
    <g id="i-eye"><ellipse cx="7" cy="4.5" rx="6.5" ry="3.5" fill="none" stroke="#555"/><circle cx="7" cy="4.5" r="1.6" fill="#555"/></g>
    <g id="i-chat"><path d="M1 1h10v6H5L2 9V7H1z" fill="#555"/><path d="M3 3h6M3 5h4" stroke="#fff" stroke-width=".8"/></g>
    <g id="i-cal"><rect x="1" y="4" width="18" height="14" fill="none" stroke="#fff" stroke-width="1.3"/><path d="M1 8h18M6 1v5M14 1v5M5 11h2M9 11h2M13 11h2M5 14h2M9 14h2M13 14h2" stroke="#fff" stroke-width="1.3"/></g>
  </defs>
</svg>

<article class="abs listing" style="top:286px">
  <div class="photo ph-facade" role="img" aria-label="Lit entrance of a stone apartment building at dusk"></div>
  <h3>House Ciro , Egypt</h3><div class="stars">★★★★★★★</div>
  <p>It is a long established fact that a reader will be distracted by the readable content of a page when looking at its layout. The point of using</p>
  <div class="meta"><span><svg width="14" height="9"><use href="#i-bed"/></svg>: 5</span><span><svg width="13" height="10"><use href="#i-bath"/></svg>: 2</span><span><svg width="14" height="9"><use href="#i-eye"/></svg>: 50000</span><span><svg width="12" height="10"><use href="#i-chat"/></svg>: 50000</span></div>
  <div class="btn btn-green book"><svg width="20" height="19"><use href="#i-cal"/></svg></div>
  <div class="btn btn-red price">100$</div>
</article>

<article class="abs listing" style="top:380px">
  <div class="photo ph-chalet" role="img" aria-label="Stone mountain chalet with terrace and snowy peaks"></div>
  <h3>House Ciro , Egypt</h3><div class="stars">★★★★★★★</div>
  <p>It is a long established fact that a reader will be distracted by the readable content of a page when looking at its layout. The point of using</p>
  <div class="meta"><span><svg width="14" height="9"><use href="#i-bed"/></svg>: 5</span><span><svg width="13" height="10"><use href="#i-bath"/></svg>: 2</span><span><svg width="14" height="9"><use href="#i-eye"/></svg>: 50000</span><span><svg width="12" height="10"><use href="#i-chat"/></svg>: 50000</span></div>
  <div class="btn btn-green book"><svg width="20" height="19"><use href="#i-cal"/></svg></div>
  <div class="btn btn-red price">100$</div>
</article>

<article class="abs listing" style="top:474px">
  <div class="photo ph-villa" role="img" aria-label="Modern villa with lit windows at dusk"></div>
  <h3>House Ciro , Egypt</h3><div class="stars">★★★★★★★</div>
  <p>It is a long established fact that a reader will be distracted by the readable content of a page when looking at its layout. The point of using</p>
  <div class="meta"><span><svg width="14" height="9"><use href="#i-bed"/></svg>: 5</span><span><svg width="13" height="10"><use href="#i-bath"/></svg>: 2</span><span><svg width="14" height="9"><use href="#i-eye"/></svg>: 50000</span><span><svg width="12" height="10"><use href="#i-chat"/></svg>: 50000</span></div>
  <div class="btn btn-green book"><svg width="20" height="19"><use href="#i-cal"/></svg></div>
  <div class="btn btn-red price">100$</div>
</article>

<article class="abs listing" style="top:568px">
  <div class="photo ph-lounge" role="img" aria-label="Bright living room with blue sofa and colourful artwork"></div>
  <h3>House Ciro , Egypt</h3><div class="stars">★★★★★★★</div>
  <p>It is a long established fact that a reader will be distracted by the readable content of a page when looking at its layout. The point of using</p>
  <div class="meta"><span><svg width="14" height="9"><use href="#i-bed"/></svg>: 5</span><span><svg width="13" height="10"><use href="#i-bath"/></svg>: 2</span><span><svg width="14" height="9"><use href="#i-eye"/></svg>: 50000</span><span><svg width="12" height="10"><use href="#i-chat"/></svg>: 50000</span></div>
  <div class="btn btn-green book"><svg width="20" height="19"><use href="#i-cal"/></svg></div>
  <div class="btn btn-red price">100$</div>
</article>

<article class="abs listing" style="top:661px">
  <div class="photo ph-villa" role="img" aria-label="Modern villa with lit windows at dusk"></div>
  <h3>House Ciro , Egypt</h3><div class="stars">★★★★★★★</div>
  <p>It is a long established fact that a reader will be distracted by the readable content of a page when looking at its layout. The point of using</p>
  <div class="meta"><span><svg width="14" height="9"><use href="#i-bed"/></svg>: 5</span><span><svg width="13" height="10"><use href="#i-bath"/></svg>: 2</span><span><svg width="14" height="9"><use href="#i-eye"/></svg>: 50000</span><span><svg width="12" height="10"><use href="#i-chat"/></svg>: 50000</span></div>
  <div class="btn btn-green book"><svg width="20" height="19"><use href="#i-cal"/></svg></div>
  <div class="btn btn-red price">100$</div>
</article>

<article class="abs listing" style="top:755px">
  <div class="photo ph-lounge" role="img" aria-label="Bright living room with blue sofa and colourful artwork"></div>
  <h3>House Ciro , Egypt</h3><div class="stars">★★★★★★★</div>
  <p>It is a long established fact that a reader will be distracted by the readable content of a page when looking at its layout. The point of using</p>
  <div class="meta"><span><svg width="14" height="9"><use href="#i-bed"/></svg>: 5</span><span><svg width="13" height="10"><use href="#i-bath"/></svg>: 2</span><span><svg width="14" height="9"><use href="#i-eye"/></svg>: 50000</span><span><svg width="12" height="10"><use href="#i-chat"/></svg>: 50000</span></div>
  <div class="btn btn-green book"><svg width="20" height="19"><use href="#i-cal"/></svg></div>
  <div class="btn btn-red price">100$</div>
</article>

<article class="abs listing" style="top:849px">
  <div class="photo ph-lounge" role="img" aria-label="Bright living room with blue sofa and colourful artwork"></div>
  <h3>House Ciro , Egypt</h3><div class="stars">★★★★★★★</div>
  <p>It is a long established fact that a reader will be distracted by the readable content of a page when looking at its layout. The point of using</p>
  <div class="meta"><span><svg width="14" height="9"><use href="#i-bed"/></svg>: 5</span><span><svg width="13" height="10"><use href="#i-bath"/></svg>: 2</span><span><svg width="14" height="9"><use href="#i-eye"/></svg>: 50000</span><span><svg width="12" height="10"><use href="#i-chat"/></svg>: 50000</span></div>
  <div class="btn btn-green book"><svg width="20" height="19"><use href="#i-cal"/></svg></div>
  <div class="btn btn-red price">100$</div>
</article>

<nav class="abs pager">
  <span><svg width="6" height="8"><path d="M5 1L2 4l3 3" fill="none" stroke="#333" stroke-width="1.5"/></svg></span>
  <span>1</span><span>2</span><span class="on">3</span><span>4</span><span>5</span>
  <span><svg width="6" height="8"><path d="M1 1l3 3-3 3" fill="none" stroke="#333" stroke-width="1.5"/></svg></span>
</nav>

<footer class="abs footer">
  <h4 style="left:74px">Links</h4>
  <ul style="left:74px"><li>Home</li><li>Groups</li><li>Sales conditions</li><li>Contact</li><li>My account</li><li>Login</li></ul>
  <ul style="left:165px"><li>Join a group</li><li>Create a group</li><li>Look for a house/appartement</li><li>My profile</li><li>My account</li><li>My groups OR my properties</li></ul>
  <h4 style="left:314px">Our mission</h4>
  <p class="mission">It is a long established fact that a reader will be distracted by the readable content of a page when looking at its layout. The point of using Lorem Ipsum is that it has a more-or-less</p>
  <div class="abs socials" style="left:472px;top:42px">
    <span style="background:#f26b2b"></span><span style="background:#d9392c"></span><span style="background:#1f6fa8"></span><span style="background:#356a9a"></span><span style="background:#4cb050"></span><span style="background:#dc4b3e"></span><span style="background:#2aa9e0"></span><span style="background:#ea5a6e"></span><span style="background:#3b5998"></span>
  </div>
  <div class="contact-line" style="top:54px"><svg width="11" height="8"><rect x=".5" y=".5" width="10" height="7" fill="#fff"/><path d="M.5 .5l5 4 5-4" fill="none" stroke="#148c9f"/></svg>hello@lanternnest.example</div>
  <div class="contact-line" style="top:66px"><svg width="11" height="8"><rect x=".5" y=".5" width="10" height="7" fill="#fff"/><path d="M.5 .5l5 4 5-4" fill="none" stroke="#148c9f"/></svg>hello@lanternnest.example</div>
  <div class="contact-line" style="top:80px;left:474px">copy rihgt 2017</div>
  <div class="abs foot-lang">English ⌄</div>
</footer>

</body>
</html>
```